Eco retreat in Whitsundays Coral Shelf

Would like a web design for letting this holiday property. It is available on lodgra see https://www.lodgra.example/accommodation/qld/whitsundays/cove-point/57203
and NestLet https://www.nestlet.example/rooms/7190364
I also want it to have its' own website for bookings with a calendar and email inquiry. Can use images and wording from lodgra or Nest Let sites.
The existing facility is the main house with plans for expansion with eco-treehouses and beach chalets. So can you sue picture of the bedrooms and lounges. The colours are amazing.
Updates

Project Deadline Extended
Reason: My apologies but I have been doing landscaping up on the property and wanted to provide additional images. I will attach these to the brief.

Target Market(s)

Is middle to upper income people who love nature, quietness, exercise

Industry/Entity Type

Accommodation

Coding

Coded - Design and coding required

Number of Pages Required

3 page

Font styles to use
Sans Serif

Colors
33b8a4
ffc214
0692cd

Requirements
Must have
• Main page that provides the overall ambience and ability to book quickly
• 2 nd page with the activities (diving, riding) and house facilities (pictures of the rooms and lounges)
• 3 rd page would be the location and logistics of getting there
Nice to have
• Simplicity through images and key phrases that invites connection
Should not have
• too much text

```html
<!DOCTYPE html>
<html lang="en">
<head>
<meta charset="utf-8">
<title>Kestrel Grove Eco Retreat</title>
<link href="https://fonts.googleapis.com/css2?family=Open+Sans:wght@400;600;700&family=Roboto+Condensed:wght@400;700&display=swap" rel="stylesheet">
<style>
:root{
  --teal:#33b8a4;
  --teal-dark:#2a9a89;
  --sun:#ffc214;
  --ocean:#0692cd;
  --ink:#333333;
  --muted:#666666;
  --light:#f3f3f3;
  --navy:#1f3346;
  --navy-deep:#152433;
  --charcoal:#2f2f2f;
  --footer:#1c1c1c;
  --footer-text:#b5b5b5;
  --white:#ffffff;
  --num-grey:#cfcfcf;
}
*{margin:0;padding:0;box-sizing:border-box}
html,body{width:1200px;height:2765px;overflow:hidden}
body{font-family:"Open Sans",Arial,sans-serif;color:var(--ink);background:var(--white);position:relative}
.abs{position:absolute}

/* hero */
.hero{position:absolute;left:0;top:0;width:1200px;height:520px;overflow:hidden}
.hero-photo{position:absolute;inset:0;background:
  linear-gradient(180deg,rgba(10,30,40,.6) 0,rgba(0,0,0,0) 90px),
  linear-gradient(100deg,#6f6a5e 0%,#a39c8b 22%,#8a8376 40%,#4f8f95 60%,#2f96a0 78%,#5fa9a8 100%)}
.brand{position:absolute;left:157px;top:26px;display:flex;align-items:center;gap:10px;color:var(--white);font-weight:700;font-size:15px;letter-spacing:.3px}
.brand-dot{width:30px;height:30px;border-radius:50%;background:var(--teal)}
.topinfo{position:absolute;left:360px;top:8px;width:683px;height:30px;border-bottom:1px solid rgba(255,255,255,.3);display:flex;align-items:center;font-size:10px;color:var(--white)}
.topinfo span{display:flex;align-items:center;gap:6px;margin-right:26px}
.topinfo .call{margin-left:auto;margin-right:0;font-weight:700;font-size:12px}
.topinfo .call b{color:var(--sun)}
.nav{position:absolute;left:522px;top:46px;display:flex;font-size:10.5px;font-weight:600;color:var(--white)}
.nav a{color:inherit;text-decoration:none;margin-right:26px;padding-bottom:6px}
.nav a.active{color:var(--sun);border-bottom:2px solid var(--sun)}
.hero-title{position:absolute;left:230px;top:205px;font-size:29px;font-weight:700;color:var(--white);line-height:33px}
.hero-title em{font-style:normal;color:var(--sun)}
.price-badge{position:absolute;left:774px;top:146px;width:184px;height:184px;border-radius:50%;background:var(--teal);border:6px solid rgba(255,255,255,.45);background-clip:padding-box;color:var(--white);text-align:center;padding-top:28px}
.price-badge .from{font-size:12px;margin-top:4px}
.price-badge .rate{font-size:22px;font-weight:700;margin-top:4px}
.price-badge .min{font-size:10px;font-weight:700;margin-top:4px}
.hero-arrow{position:absolute;top:298px}
.search{position:absolute;left:157px;top:406px;width:886px;height:66px;background:rgba(255,255,255,.25);padding:12px;display:flex;gap:8px}
.field{background:var(--white);height:42px;display:flex;align-items:center;gap:8px;padding:0 12px;font-size:10px;color:#888}
.f-where{width:286px}.f-date{width:136px}.f-guest{width:136px;justify-content:space-between}
.btn-search{flex:1;background:var(--ocean);color:var(--white);font-weight:700;font-size:12px;display:flex;align-items:center;justify-content:center}

/* headings */
.sec-title{position:absolute;left:0;width:1200px;text-align:center;font-size:19px;font-weight:600;color:var(--ink)}
.sec-title::after{content:"";display:block;width:52px;height:2px;background:var(--teal);margin:18px auto 0}
.btn-ghost{position:absolute;left:536px;width:128px;height:30px;background:#f1f1f1;border-left:3px solid var(--teal);border-right:3px solid var(--teal);font-size:10px;font-weight:600;display:flex;align-items:center;justify-content:center;color:var(--ink)}

/* about */
.about-text{position:absolute;left:290px;top:627px;width:620px;text-align:center;font-size:10.5px;line-height:18px;color:var(--muted)}

/* facilities */
.facilities{position:absolute;left:0;top:824px;width:1200px;height:282px;background:var(--light)}
.fac{position:absolute;top:118px;width:226px;text-align:center}
.fac .num{font-family:"Roboto Condensed",Arial,sans-serif;font-size:76px;font-weight:700;color:var(--num-grey);line-height:76px}
.fac .lbl{font-size:12px;color:var(--muted);display:flex;justify-content:center;align-items:center;gap:6px;margin-top:10px}
.fac.on .num,.fac.on .lbl{color:var(--teal)}
.fac-sep{position:absolute;top:115px;width:1px;height:125px;background:#dddddd}

/* how it works */
.how{position:absolute;left:0;top:1106px;width:1200px;height:448px;background:radial-gradient(ellipse at 50% 55%,#27445a 0%,var(--navy) 55%,var(--navy-deep) 100%)}
.how .sec-title{color:var(--white);top:46px}
.step{position:absolute;width:240px;font-size:10.5px;line-height:16px;color:var(--white)}
.step h3{font-size:12.5px;font-weight:600;color:var(--sun);letter-spacing:.5px;margin-bottom:14px}
.step.l{text-align:right}

/* packages */
.card{position:absolute;top:1666px;width:280px;height:324px;background:var(--white);box-shadow:0 0 6px rgba(0,0,0,.12)}
.card.raised{box-shadow:0 3px 14px rgba(0,0,0,.28)}
.card-tag{position:absolute;left:18px;top:12px;width:244px;height:28px;background:var(--teal);color:var(--white);font-size:12px;font-weight:700;padding:6px 10px}
.card-photo{position:absolute;left:18px;top:40px;width:244px;height:106px}
.stars{position:absolute;left:18px;top:160px;display:flex;gap:3px}
.card-text{position:absolute;left:18px;top:183px;width:244px;font-size:10px;line-height:15px;color:var(--muted)}
.card-rule{position:absolute;left:18px;top:227px;width:244px;height:1px;background:#e6e6e6}
.card-price{position:absolute;left:18px;top:246px;font-size:10px;color:var(--ink)}
.card-price b{display:block;font-size:16px;font-weight:400;margin-top:2px}
.card-price s{color:#999}
.card-bar{position:absolute;left:0;bottom:0;width:280px;height:33px;background:var(--charcoal);color:var(--white);font-size:10px;font-weight:700;padding:10px 16px}
.card-bar i{position:absolute;right:0;top:0;width:76px;height:33px;background:var(--teal);clip-path:polygon(22px 0,100% 0,100% 100%,0 100%);display:flex;align-items:center;justify-content:center}
.pager{position:absolute;top:1800px;width:34px;height:34px;border-radius:50%;border:1.5px solid var(--teal);display:flex;align-items:center;justify-content:center}

/* newsletter */
.news{position:absolute;left:0;top:2123px;width:1200px;height:262px;background:linear-gradient(90deg,#22392f 0%,#2e4a3a 45%,#20352b 70%,#2b4636 100%)}
.family-photo{position:absolute;left:92px;top:2055px;width:516px;height:330px;background:linear-gradient(180deg,rgba(214,176,140,0) 0%,rgba(205,165,128,.75) 30%,rgba(190,150,115,.85) 70%,rgba(150,120,90,.6) 100%)}
.news-title{position:absolute;left:612px;top:2170px;font-size:25px;font-weight:700;color:var(--white)}
.news-title em{font-style:normal;color:var(--sun)}
.news-text{position:absolute;left:612px;top:2210px;width:380px;font-size:10px;line-height:14px;color:var(--white)}
.input{position:absolute;top:2254px;width:176px;height:28px;border:1px solid rgba(255,255,255,.7);color:var(--white);font-size:10px;padding:7px 10px}
.btn-send{position:absolute;left:612px;top:2298px;width:94px;height:30px;background:var(--ocean);color:var(--white);font-size:10px;font-weight:600;display:flex;align-items:center;justify-content:center;gap:6px}

/* footer */
.footer{position:absolute;left:0;top:2385px;width:1200px;height:380px;background:var(--footer);color:var(--footer-text)}
.f-col{position:absolute;top:60px}
.f-head{display:flex;align-items:center;gap:12px;color:var(--white);font-size:13px;font-weight:600;letter-spacing:.4px}
.f-icon{width:36px;height:36px;border-radius:50%;background:#e9e9e9;display:flex;align-items:center;justify-content:center}
.f-line{position:absolute;top:40px;width:1px;height:230px;background:#3c3c3c}
.f-list{list-style:none;margin:22px 0 0 46px;font-size:10.5px;line-height:21px}
.f-list li::before{content:"»";margin-right:10px;color:var(--footer-text)}
.f-list li.on{color:var(--teal)}
.f-addr{margin:22px 0 0 46px;font-size:10.5px;line-height:17px}
.social{display:flex;gap:14px;margin:18px 0 0 46px}
.social span{width:11px;height:11px;border-radius:50%;background:var(--footer-text)}
.f-bottom{position:absolute;left:0;top:315px;width:1200px;height:1px;background:#303030}
.copy{position:absolute;left:157px;top:343px;font-size:10.5px;color:var(--footer-text)}
.up{position:absolute;left:1000px;top:333px;width:34px;height:34px;border-radius:50%;border:1.5px solid var(--teal);display:flex;align-items:center;justify-content:center}
</style>
</head>
<body>

<svg width="0" height="0" style="position:absolute"><defs><path id="st" d="M5 0l1.5 3.3 3.5.3-2.7 2.3.8 3.5L5 7.6 1.9 9.4l.8-3.5L0 3.6l3.5-.3z"/></defs></svg>

<header class="hero">
  <div class="hero-photo" role="img" aria-label="Photo of a woman walking down a timber boardwalk towards a sandy beach and turquoise water"></div>
  <div class="brand"><span class="brand-dot"></span>KESTREL GROVE</div>
  <div class="topinfo">
    <span><svg width="8" height="10" viewBox="0 0 8 10"><path d="M4 0a4 4 0 0 0-4 4c0 3 4 6 4 6s4-3 4-6a4 4 0 0 0-4-4zm0 5.5A1.5 1.5 0 1 1 4 2.5a1.5 1.5 0 0 1 0 3z" fill="#fff"/></svg>48 palm row, airlie, qld</span>
    <span><svg width="11" height="8" viewBox="0 0 11 8"><rect x=".5" y=".5" width="10" height="7" fill="none" stroke="#fff"/><path d="M.5.5l5 4 5-4" fill="none" stroke="#fff"/></svg>hello@kestrelgrove.example</span>
    <span class="call">CALL US:&nbsp;<b>+61 400 000 000</b></span>
  </div>
  <nav class="nav">
    <a class="active">HOME</a><a>FEATURES ▾</a><a>ABOUT US</a><a>LISTING ▾</a><a>GALLERY</a><a>BLOG</a><a>CONTACTS</a>
  </nav>
  <h1 class="hero-title">Book with <em>confidence,</em><br><em>Travel</em> with peace of mind.</h1>
  <div class="price-badge">
    <svg width="40" height="34" viewBox="0 0 40 34"><path d="M20 2L2 18h5v14h10v-9h6v9h10V18h5z" fill="#fff"/></svg>
    <div class="from">From</div>
    <div class="rate">$345 / night</div>
    <div class="min">Min 3 nights stay</div>
  </div>
  <svg class="hero-arrow" style="left:58px" width="22" height="44" viewBox="0 0 22 44"><path d="M20 2L2 22l18 20" fill="none" stroke="#fff" stroke-width="2"/></svg>
  <svg class="hero-arrow" style="left:1120px" width="22" height="44" viewBox="0 0 22 44"><path d="M2 2l18 20L2 42" fill="none" stroke="#fff" stroke-width="2"/></svg>
  <form class="search">
    <div class="field f-where"><svg width="8" height="10" viewBox="0 0 8 10"><path d="M4 0a4 4 0 0 0-4 4c0 3 4 6 4 6s4-3 4-6a4 4 0 0 0-4-4z" fill="#33b8a4"/></svg>Where do you want to go ?</div>
    <div class="field f-date"><svg width="10" height="10" viewBox="0 0 10 10"><rect x=".5" y="1.5" width="9" height="8" fill="none" stroke="#aaa"/><path d="M.5 4h9" stroke="#aaa"/></svg>Check In</div>
    <div class="field f-date"><svg width="10" height="10" viewBox="0 0 10 10"><rect x=".5" y="1.5" width="9" height="8" fill="none" stroke="#aaa"/><path d="M.5 4h9" stroke="#aaa"/></svg>Check Out</div>
    <div class="field f-guest"><span style="display:flex;gap:8px;align-items:center"><svg width="9" height="10" viewBox="0 0 9 10"><circle cx="4.5" cy="3" r="2.5" fill="#aaa"/><path d="M0 10a4.5 4 0 0 1 9 0z" fill="#aaa"/></svg>Guests</span>▾</div>
    <div class="btn-search">Search</div>
  </form>
</header>

<section>
  <h2 class="sec-title" style="top:563px">About Kestrel Grove Eco Retreat</h2>
  <p class="about-text">This is the place for your special getaway, as a couple celebrating a special occasion, up to 4 couples on a group holiday, or a small family reunion.<br>The house was designed by a renowned tropical architect, and sits on 5 acres of secluded bushland with direct NE beach frontage. There is great fishing and snorkelling on the fringing reef just offshore, which can also be explored by reef-walking at low tide.</p>
  <div class="btn-ghost" style="top:746px">Read More</div>
</section>

<section class="facilities">
  <h2 class="sec-title" style="top:42px">Our Facilities</h2>
  <div class="fac" style="left:144px"><div class="num">08</div><div class="lbl"><svg width="14" height="10" viewBox="0 0 14 10"><circle cx="4" cy="3" r="2.5" fill="#666"/><circle cx="10" cy="3" r="2.5" fill="#666"/><path d="M0 10a4 3.5 0 0 1 8 0zM6 10a4 3.5 0 0 1 8 0z" fill="#666"/></svg>GUESTS</div></div>
  <div class="fac-sep" style="left:371px"></div>
  <div class="fac on" style="left:371px"><div class="num">04</div><div class="lbl"><svg width="8" height="11" viewBox="0 0 8 11"><path d="M1 0h6v11H1z" fill="none" stroke="#33b8a4"/></svg>BEDROOMS</div></div>
  <div class="fac-sep" style="left:598px"></div>
  <div class="fac" style="left:598px"><div class="num">05</div><div class="lbl"><svg width="14" height="9" viewBox="0 0 14 9"><path d="M0 0v9M0 6h14v3M4 3h10v3" stroke="#666" fill="none" stroke-width="1.5"/></svg>BEDS</div></div>
  <div class="fac-sep" style="left:826px"></div>
  <div class="fac" style="left:826px"><div class="num">03</div><div class="lbl"><svg width="12" height="11" viewBox="0 0 12 11"><path d="M0 5h12v2a4 4 0 0 1-4 4H4a4 4 0 0 1-4-4zM2 5V1h3" fill="#666" stroke="#666"/></svg>BATHROOMS</div></div>
</section>

<section class="how">
  <h2 class="sec-title">How Kestrel Grove Works?</h2>
  <svg class="abs" style="left:451px;top:99px" width="300" height="300" viewBox="0 0 300 300">
    <circle cx="150" cy="150" r="112" fill="#13202c"/>
    <circle cx="150" cy="150" r="138" fill="none" stroke="#33b8a4" stroke-width="2" stroke-dasharray="160 57" stroke-dashoffset="20"/>
    <circle cx="150" cy="150" r="34" fill="none" stroke="#33b8a4" stroke-width="2"/>
    <circle cx="52" cy="62" r="28" fill="#33b8a4"/>
    <circle cx="240" cy="62" r="28" fill="#33b8a4"/>
    <circle cx="52" cy="246" r="28" fill="#33b8a4"/>
    <circle cx="240" cy="246" r="28" fill="#33b8a4"/>
    <path d="M52 50l-8 12h5l-6 8h18l-6-8h5z M50 70h4v5h-4z" fill="#fff"/>
    <rect x="231" y="54" width="18" height="16" rx="2" fill="none" stroke="#fff" stroke-width="2"/>
    <path d="M235 62l4 4 6-7" fill="none" stroke="#fff" stroke-width="2"/>
    <path d="M41 250l22-12-4 8 4 8-22-4 6-2z" fill="#fff"/>
    <rect x="231" y="242" width="18" height="10" rx="2" fill="#fff"/>
    <rect x="235" y="236" width="10" height="5" fill="#fff"/>
    <rect x="235" y="253" width="10" height="6" fill="#fff"/>
  </svg>
  <div class="step l" style="left:197px;top:124px"><h3>EXPLORE DESTINATION</h3>Browse the reef, rainforest trails and quiet beaches around the retreat.</div>
  <div class="step" style="left:763px;top:124px"><h3>CHECK AVAILABILITY</h3>Pick your dates on the calendar and see open nights at a glance.</div>
  <div class="step l" style="left:197px;top:309px"><h3>GET READY FOR YOUR PLACE</h3>Receive directions, arrival tips and a packing list before you travel.</div>
  <div class="step" style="left:763px;top:309px"><h3>BOOK ONLINE</h3>Confirm your stay securely or send us an email inquiry in minutes.</div>
</section>

<section>
  <h2 class="sec-title" style="top:1597px">Kestrel Grove Packages</h2>
  <div class="pager" style="left:97px"><svg width="12" height="10" viewBox="0 0 12 10"><path d="M6 1L2 5l4 4M10 1L6 5l4 4" fill="none" stroke="#33b8a4" stroke-width="1.5"/></svg></div>
  <div class="pager" style="left:1067px"><svg width="12" height="10" viewBox="0 0 12 10"><path d="M2 1l4 4-4 4M6 1l4 4-4 4" fill="none" stroke="#33b8a4" stroke-width="1.5"/></svg></div>

  <article class="card" style="left:157px">
    <div class="card-tag">FOR COUPLES</div>
    <div class="card-photo" role="img" aria-label="Photo of a couples bedroom with timber walls and garden view" style="background:linear-gradient(120deg,#3d2a1c,#6b4a30 45%,#8a7a55 70%,#4a3a2a)"></div>
    <div class="stars"><svg width="62" height="10" viewBox="0 0 62 10"><g fill="#ffc214"><use href="#st"/><use href="#st" x="13"/><use href="#st" x="26"/></g><g fill="none" stroke="#ffc214" stroke-width=".8"><use href="#st" x="39"/><use href="#st" x="52"/></g></svg></div>
    <p class="card-text">A private bedroom with garden views, breakfast hamper and sunset drinks.</p>
    <div class="card-rule"></div>
    <div class="card-price">Price From:<b>$300 &nbsp;/ <s>$400</s></b></div>
    <div class="card-bar">SAVE $100<i><svg width="14" height="12" viewBox="0 0 14 12"><path d="M0 6h12M7 1l5 5-5 5" fill="none" stroke="#fff" stroke-width="2"/></svg></i></div>
  </article>

  <article class="card raised" style="left:461px">
    <div class="card-tag">FOR FAMILY</div>
    <div class="card-photo" role="img" aria-label="Photo of a family bedroom with patterned bedspread and open windows" style="background:linear-gradient(120deg,#4a2e22,#7a5238 40%,#b08a5a 65%,#5a4030)"></div>
    <div class="stars"><svg width="62" height="10" viewBox="0 0 62 10"><g fill="#ffc214"><use href="#st"/><use href="#st" x="13"/><use href="#st" x="26"/></g><g fill="none" stroke="#ffc214" stroke-width=".8"><use href="#st" x="39"/><use href="#st" x="52"/></g></svg></div>
    <p class="card-text">Room for the whole family, snorkel gear and easy beach access.</p>
    <div class="card-rule"></div>
    <div class="card-price">Price From:<b>$350 &nbsp;/ <s>$400</s></b></div>
    <div class="card-bar">SAVE $50<i><svg width="14" height="12" viewBox="0 0 14 12"><path d="M0 6h12M7 1l5 5-5 5" fill="none" stroke="#fff" stroke-width="2"/></svg></i></div>
  </article>

  <article class="card" style="left:763px">
    <div class="card-tag">FOR GROUPS</div>
    <div class="card-photo" role="img" aria-label="Photo of the timber main house with a red roof among tropical trees" style="background:linear-gradient(180deg,#b9cbd8 0%,#a9b8b0 35%,#7a5a45 55%,#5a6a3a 80%,#4a5a30)"></div>
    <div class="stars"><svg width="62" height="10" viewBox="0 0 62 10"><g fill="#ffc214"><use href="#st"/><use href="#st" x="13"/><use href="#st" x="26"/></g><g fill="none" stroke="#ffc214" stroke-width=".8"><use href="#st" x="39"/><use href="#st" x="52"/></g></svg></div>
    <p class="card-text">The whole main house for up to eight guests, with shared lounges.</p>
    <div class="card-rule"></div>
    <div class="card-price">Price From:<b>$200 &nbsp;/ <s>$400</s></b></div>
    <div class="card-bar">SAVE $200<i><svg width="14" height="12" viewBox="0 0 14 12"><path d="M0 6h12M7 1l5 5-5 5" fill="none" stroke="#fff" stroke-width="2"/></svg></i></div>
  </article>

  <div class="btn-ghost" style="top:2042px">Explore More</div>
</section>

<section class="news" role="img" aria-label="Background photo of a sandy clearing with tropical palms and bushland"></section>
<div class="family-photo" role="img" aria-label="Photo of a smiling family of four piggybacking outdoors"></div>
<h2 class="news-title">Subscribe to <em>Newsletter</em></h2>
<p class="news-text">Be the first to see the latest stay deals, news, features &amp; more.<br>Enter email address.</p>
<div class="input" style="left:612px">Your Name</div>
<div class="input" style="left:796px">Your Email</div>
<div class="btn-send"><svg width="10" height="10" viewBox="0 0 10 10"><path d="M0 5l10-5-3 10-2-4z" fill="#fff"/></svg>SEND</div>

<footer class="footer">
  <div class="f-line" style="left:175px"></div>
  <div class="f-line" style="left:483px"></div>
  <div class="f-line" style="left:759px"></div>
  <div class="f-col" style="left:157px">
    <div class="f-head"><span class="f-icon"><span style="width:14px;height:14px;border-radius:50%;background:var(--teal)"></span></span>KESTREL GROVE ECO RETREAT</div>
    <p class="f-addr">12 Shoreline Drive, Cove Point,<br>Queensland, AU<br><br>Email :<br>stay@kestrelgrove.example</p>
    <div class="social"><span></span><span></span><span></span><span></span><span></span><span></span></div>
  </div>
  <div class="f-col" style="left:461px">
    <div class="f-head"><span class="f-icon"><svg width="16" height="16" viewBox="0 0 16 16"><path d="M7 9l-2 2a2.5 2.5 0 0 1-3.5-3.5l2-2M9 7l2-2a2.5 2.5 0 0 1 3.5 3.5l-2 2M6 10l4-4" fill="none" stroke="#33b8a4" stroke-width="1.8"/></svg></span>QUICK LINKS</div>
    <ul class="f-list"><li class="on">Home</li><li>Features</li><li>About us</li><li>Listing</li><li>Gallery</li><li>Blog</li><li>Contacts</li></ul>
  </div>
  <div class="f-col" style="left:737px">
    <div class="f-head"><span class="f-icon"><svg width="16" height="14" viewBox="0 0 16 14"><path d="M0 1h3M5 1h11M0 7h3M5 7h11M0 13h3M5 13h11" stroke="#33b8a4" stroke-width="2"/></svg></span>FEATURES</div>
    <ul class="f-list"><li>Air conditioning</li><li>Dishwasher</li><li>Parking</li><li>Washing machine</li><li>Kitchen</li><li>Lawn/Garden</li><li>Linens provided</li></ul>
  </div>
  <div class="f-bottom"></div>
  <p class="copy">© Kestrel Grove Eco Retreat 2016, All Rights Reserved.</p>
  <div class="up"><svg width="12" height="12" viewBox="0 0 12 12"><path d="M6 11V1M1 6l5-5 5 5" fill="none" stroke="#33b8a4" stroke-width="2"/></svg></div>
</footer>

</body>
</html>
```